Industrial Project Sign

We need an eye catching (but professional) industrial project sign that will be very large (roughly 12' high x 18' wide). This sign will be highly visible from the adjacent high speed highway.

* The following needs to be at the bottom of the signage: Logo (uploaded), Name (Halvern Land Holdings, Inc.) (uploaded) and phone number (555)739-2864

*Name of Project - "Marrowfield Logistics Park"

* Text items
Land for Sale
Build to Suit
Zoning: Industrial (G I & L I)

* Interesting background that is eye catching

Good morning all,

We are considering all designers options as we go and are waiting for the final designs to come in by the 4th so that we can give each one a good look.   If you have any new designs, questions, further design options or any tweeks you want to do to current designs, please do so at this time.

Thanks to all of you for your submissions.

Industrial

```html
<!DOCTYPE html>
<html lang="en">
<head>
<meta charset="utf-8">
<title>Marrowfield Logistics Park – Project Sign</title>
<link rel="stylesheet" href="https://fonts.googleapis.com/css2?family=Source+Sans+3:wght@600;700&display=swap">
<style>
  :root {
    --brand-red: #6f1212;
    --panel-white: rgba(255, 255, 255, 0.62);
    --band-white: #ffffff;
    --glass-deep: #1f4f8c;
    --glass-mid: #3f78b8;
    --glass-light: #a9c6e4;
    --crane-red: #c8303f;
    --crane-dark: #8e1c26;
    --text-light: #ffffff;
  }
  html, body {
    margin: 0;
    padding: 0;
    overflow: hidden;
    background: #ffffff;
  }
  .sign {
    position: relative;
    width: 1200px;
    height: 800px;
    overflow: hidden;
    font-family: "Source Sans 3", "Myriad Pro", Arial, sans-serif;
  }
  .sign__backdrop {
    position: absolute;
    inset: 0;
    background:
      radial-gradient(ellipse 260px 340px at 290px 470px, rgba(200, 48, 63, 0.95) 0%, rgba(200, 48, 63, 0.75) 45%, rgba(200, 48, 63, 0) 100%),
      linear-gradient(-16deg, rgba(200, 48, 63, 0) 38%, rgba(200, 48, 63, 0.85) 47%, rgba(142, 28, 38, 0.9) 53%, rgba(200, 48, 63, 0.8) 59%, rgba(200, 48, 63, 0) 68%),
      linear-gradient(90deg, var(--glass-deep) 0%, var(--glass-mid) 45%, var(--glass-mid) 70%, var(--glass-light) 100%);
  }
  .project-title {
    position: absolute;
    left: 0;
    top: 28px;
    width: 741px;
    height: 115px;
    margin: 0;
    padding-left: 42px;
    box-sizing: border-box;
    background: var(--brand-red);
    color: var(--text-light);
    font-weight: 600;
    font-size: 50px;
    line-height: 115px;
    white-space: nowrap;
  }
  .offer-panel {
    position: absolute;
    left: 682px;
    top: 227px;
    width: 518px;
    height: 268px;
    background: var(--panel-white);
    box-sizing: border-box;
    padding: 16px 0 0 31px;
  }
  .offer-panel__list {
    margin: 0;
    padding: 0;
    list-style: none;
    color: var(--brand-red);
    font-weight: 700;
    font-size: 48px;
    line-height: 58px;
    white-space: nowrap;
  }
  .contact-band {
    position: absolute;
    left: 0;
    top: 581px;
    width: 1200px;
    height: 157px;
    background: var(--band-white);
  }
  .company__mark {
    position: absolute;
    left: 48px;
    top: 22px;
    width: 112px;
    height: 112px;
    background: var(--brand-red);
  }
  .company__name {
    position: absolute;
    left: 185px;
    top: 62px;
    width: 330px;
    padding-left: 8px;
    box-sizing: border-box;
    border-bottom: 3px solid var(--brand-red);
    color: var(--brand-red);
    font-weight: 600;
    font-size: 26px;
    line-height: 32px;
    white-space: nowrap;
  }
  .phone {
    position: absolute;
    left: 638px;
    top: 30px;
    color: var(--brand-red);
    font-weight: 700;
    font-size: 76px;
    line-height: 96px;
    white-space: nowrap;
  }
</style>
</head>
<body>
  <main class="sign">
    <div class="sign__backdrop" role="img" aria-label="Photograph of a red tower crane with operator cab and long boom in front of a curved blue glass office building"></div>

    <h1 class="project-title">Marrowfield Logistics Park</h1>

    <section class="offer-panel">
      <ul class="offer-panel__list">
        <li>Land for Sale</li>
        <li>Build to Suit</li>
        <li>Zoning: Industrial</li>
        <li>(G I &amp; L I)</li>
      </ul>
    </section>

    <footer class="contact-band">
      <span class="company__mark" aria-hidden="true"></span>
      <span class="company__name">Halvern Land Holdings, Inc.</span>
      <div class="phone">(555)739-2864</div>
    </footer>
  </main>
</body>
</html>
```